A new healing and spiritual podcast needs a design.

We need a design for the podcast that will also be used on the supporting website. The name is The Quiet Lantern. The podcast will be about tapping into our own guidance to have a great life. There will be interviews, meditations, discussions on all aspects of energy healing and alternative healing techniques. The website will be where classes will be offered. Looking for something that conveys a peaceful feeling without looking too "healy-feely". Yet also want it to get peoples attention.

Target Market(s)

Metaphysical, spiritual (not religious), energy healers

Font styles to use
Serif

Requirements
Must have
• The name "The Quiet Lantern"
Nice to have
• I'd like it to be inviting, catch peoples eye, convey a peaceful feeling, yet not be boring.
Should not have
• Animated (like comic strip) images.

```html
<!DOCTYPE html>
<html lang="en">
<head>
<meta charset="utf-8">
<title>The Quiet Lantern</title>
<link rel="stylesheet" href="https://fonts.googleapis.com/css2?family=Marcellus&display=swap">
<style>
  :root {
    --sky-top: #6f2a63;
    --sky-mid: #c9557f;
    --sky-pink: #e07a9c;
    --sky-glow: #f28a4c;
    --sky-low: #8a2f5e;
    --ground: #120611;
    --veil: rgba(255, 235, 245, 0.2);
    --rule: rgba(255, 240, 245, 0.55);
    --title: #f4e6e4;
    --title-shadow: rgba(40, 8, 30, 0.75);
  }
  html, body {
    margin: 0;
    padding: 0;
    width: 1200px;
    height: 1200px;
    overflow: hidden;
    background: var(--ground);
  }
  .cover {
    position: relative;
    width: 1200px;
    height: 1200px;
    overflow: hidden;
  }
  .sky-photo {
    position: absolute;
    inset: 0;
    background:
      radial-gradient(ellipse 420px 260px at 90px 930px, var(--sky-glow) 0%, rgba(242,138,76,0) 100%),
      radial-gradient(ellipse 520px 420px at 640px 620px, var(--sky-pink) 0%, rgba(224,122,156,0) 100%),
      linear-gradient(180deg, var(--sky-top) 0%, var(--sky-mid) 40%, var(--sky-pink) 60%, var(--sky-low) 88%, var(--ground) 97%);
  }
  .veil {
    position: absolute;
    left: 63px;
    top: 89px;
    width: 1074px;
    height: 1022px;
    background: var(--veil);
  }
  .rule-top {
    position: absolute;
    left: 128px;
    top: 63px;
    width: 977px;
    border-top: 2px dashed var(--rule);
  }
  .rule-side {
    position: absolute;
    left: 1081px;
    top: 44px;
    height: 1067px;
    border-left: 2px dashed var(--rule);
  }
  .glow {
    position: absolute;
    border-radius: 50%;
    background: radial-gradient(circle, rgba(255,240,245,0.7) 0%, rgba(255,240,245,0) 70%);
  }
  .glow-center { left: 450px; top: 455px; width: 300px; height: 300px; }
  .glow-corner-top { left: 141px; top: 178px; width: 100px; height: 100px; }
  .glow-corner-bottom { left: 950px; top: 906px; width: 100px; height: 100px; }
  .title-ring {
    position: absolute;
    inset: 0;
  }
  .title-ring text {
    font-family: "Marcellus", serif;
    font-size: 82px;
    fill: var(--title);
    letter-spacing: 2px;
    filter: drop-shadow(3px 5px 5px var(--title-shadow));
  }
</style>
</head>
<body>
  <main class="cover">
    <div class="sky-photo" role="img" aria-label="Photo of a woman in silhouette dancing against a pink and purple sunset sky"></div>
    <div class="veil"></div>
    <div class="rule-top"></div>
    <div class="rule-side"></div>
    <div class="glow glow-center" role="img" aria-label="Radiant sunburst ornament"></div>
    <div class="glow glow-corner-top" role="img" aria-label="Small sparkle ornament"></div>
    <div class="glow glow-corner-bottom" role="img" aria-label="Small sparkle ornament"></div>
    <svg class="title-ring" width="1200" height="1200" viewBox="0 0 1200 1200">
      <defs>
        <path id="title-arc" d="M600,916 A311,311 0 1,1 600.1,916"/>
      </defs>
      <text>
        <textPath href="#title-arc" startOffset="185" textLength="1585" lengthAdjust="spacing">THE QUIET LANTERN</textPath>
      </text>
    </svg>
  </main>
</body>
</html>
```